KELD, Inc. new buisness cards - brand guide included

We need new business cards. SLEAK SIMPLE FINANCE. They must include a place for NAME, TITLE, CELL, OFFICE PHONE, EMAIL. they also must include our services across the bottom. AIR, OCEAN, FTL, LTL, EXPRESS. for reference this will be being handed to some of the most prestigious shipping companies in a america.

Target Market(s)

Finance and corporate

Contact Information for Business Card

We need new business cards. SLEAK SIMPLE FINANCE. They must include a place for NAME, TITLE, CELL, OFFICE PHONE, EMAIL. they also must include our services across the bottom. AIR, OCEAN, FTL, LTL, EXPRESS.

Requirements
Must have
• We need new business cards. SLEAK SIMPLE FINANCE. They must include a place for NAME, TITLE, CELL, OFFICE PHONE, EMAIL. they also must include our services across the bottom. AIR, OCEAN, FTL, LTL, EXPRESS.
Nice to have
• USE THE COLORS AND LOGO IN THE BRAND GUIDE :)

```html
<!DOCTYPE html>
<html lang="en">
<head>
<meta charset="utf-8">
<title>KELD, Inc. — Business Cards</title>
<link href="https://fonts.googleapis.com/css2?family=Montserrat:wght@400;600;700&display=swap" rel="stylesheet">
<style>
  :root {
    --backdrop: #2b2b2b;
    --card: #1f1f1f;
    --ink: #f4f2ee;
    --ink-soft: #dcdad6;
    --mark-faint: #2c2c2c;
  }
  * { box-sizing: border-box; margin: 0; padding: 0; }
  html, body { width: 1200px; height: 900px; overflow: hidden; }
  body {
    background: var(--backdrop);
    font-family: "Montserrat", sans-serif;
    color: var(--ink);
    position: relative;
  }
  .card {
    position: absolute;
    left: 250px;
    width: 700px;
    height: 400px;
    background: var(--card);
    border-radius: 18px;
    overflow: hidden;
  }
  .card--brand { top: 34px; }
  .card--contact { top: 466px; }

  /* brand side */
  .brand-mark {
    position: absolute;
    left: 0; right: 0; top: 105px;
    text-align: center;
    font-size: 110px;
    font-weight: 600;
    letter-spacing: 14px;
    color: var(--mark-faint);
  }
  .services {
    position: absolute;
    left: 0; right: 0; top: 300px;
    text-align: center;
    font-size: 19px;
    letter-spacing: 1.5px;
    color: var(--ink);
  }
  .services .dot { margin: 0 10px; }

  /* contact side */
  .name-bar {
    position: absolute;
    left: 0; top: 78px;
    width: 14px; height: 50px;
    background: var(--ink);
    border-radius: 0 4px 4px 0;
  }
  .person { position: absolute; left: 38px; top: 76px; }
  .person__name { font-size: 24px; font-weight: 700; letter-spacing: 1px; }
  .person__title { font-size: 17px; color: var(--ink-soft); margin-top: 2px; }

  .company-name {
    position: absolute;
    right: 60px; top: 46px;
    display: flex; align-items: center; gap: 14px;
    font-size: 46px; font-weight: 600; letter-spacing: 6px;
    color: var(--ink);
  }
  .company-name .square {
    width: 16px; height: 16px; background: var(--ink);
  }

  .address {
    position: absolute;
    right: 60px; top: 214px;
    text-align: right;
    font-size: 16px; line-height: 1.45;
    color: var(--ink-soft);
  }
  .accent-band {
    position: absolute;
    right: 0; top: 282px;
    width: 210px; height: 14px;
    background: var(--ink);
  }

  .contact-list {
    position: absolute;
    left: 100px; top: 262px;
    list-style: none;
    font-size: 17px; line-height: 1.6;
    color: var(--ink);
  }
  .contact-list li { display: flex; align-items: center; gap: 10px; }
  .contact-list svg { width: 14px; height: 14px; flex: none; }
</style>
</head>
<body>

  <section class="card card--brand">
    <div class="brand-mark">KELD</div>
    <p class="services">Air<span class="dot">•</span>Ocean<span class="dot">•</span>Ftl<span class="dot">•</span>Ltl<span class="dot">•</span>Express</p>
  </section>

  <section class="card card--contact">
    <div class="name-bar"></div>
    <div class="person">
      <p class="person__name">DORIAN VALE</p>
      <p class="person__title">Founder/CEO</p>
    </div>

    <div class="company-name"><span class="square"></span>KELD</div>

    <p class="address">48 B. Harbor Lane<br>Region Name, CD 4120</p>
    <div class="accent-band"></div>

    <ul class="contact-list">
      <li>
        <svg viewBox="0 0 14 14" aria-hidden="true"><rect x="3.5" y="1" width="7" height="12" rx="1.3" fill="none" stroke="#f4f2ee" stroke-width="1.3"/><circle cx="7" cy="11" r="0.8" fill="#f4f2ee"/></svg>
        418.302.7714
      </li>
      <li>
        <svg viewBox="0 0 14 14" aria-hidden="true"><path d="M3 1.5 L5.2 4 L4 5.6 C4.8 7.4 6.6 9.2 8.4 10 L10 8.8 L12.5 11 L11 12.8 C6 12.5 1.5 8 1.2 3 Z" fill="#f4f2ee"/></svg>
        418.306.5290
      </li>
      <li>
        <svg viewBox="0 0 14 14" aria-hidden="true"><rect x="1" y="3" width="12" height="8.5" fill="#f4f2ee"/><path d="M1 3 L7 8 L13 3" fill="none" stroke="#1f1f1f" stroke-width="1.1"/></svg>
        info@keldinc.com
      </li>
      <li>
        <svg viewBox="0 0 14 14" aria-hidden="true"><g fill="none" stroke="#f4f2ee" stroke-width="1.1"><circle cx="7" cy="7" r="5.8"/><ellipse cx="7" cy="7" rx="2.6" ry="5.8"/><line x1="1.2" y1="7" x2="12.8" y2="7"/><line x1="2" y1="4" x2="12" y2="4"/><line x1="2" y1="10" x2="12" y2="10"/></g></svg>
        www.keldinc.com
      </li>
    </ul>
  </section>

</body>
</html>
```